Local fast-growing company in the service sector

We are looking for a modern business card design, which should also appear on our letterheads

Target Market(s)

Private and industrial sectors

Contact Information for Business Card

Vorname Name
Kellbacher Str. 38
74819 Haldenberg
Tel.: 07162-418395-0
Name@service-tkwl.de

Colors
9d9d9d
919191
aaaaaa

Requirements
Must have
• The logo (file) in silver

```html
<!DOCTYPE html>
<html lang="de">
<head>
<meta charset="utf-8">
<title>TKWL Visitenkarte</title>
<link rel="stylesheet" href="https://fonts.googleapis.com/css2?family=Open+Sans:wght@400;600;700&display=swap">
<style>
  :root {
    --stage: #2b2b2b;
    --silver-dark: #919191;
    --silver: #9d9d9d;
    --silver-light: #aaaaaa;
    --paper: #ffffff;
    --ink: #7a7a7a;
    --rule: #b5b5b5;
  }
  * { box-sizing: border-box; margin: 0; padding: 0; }
  html, body {
    width: 1200px; height: 900px; overflow: hidden;
    background: var(--stage);
    font-family: "Open Sans", Arial, sans-serif;
  }
  .canvas { position: relative; width: 1200px; height: 900px; }
  .card {
    position: absolute; left: 290px; width: 620px; height: 360px;
    box-shadow: 0 10px 30px rgba(0,0,0,.5);
    overflow: hidden;
  }
  .card--back {
    top: 50px;
    background: radial-gradient(ellipse at 45% 35%, #d2d2d2 0%, var(--silver-light) 45%, var(--silver-dark) 100%);
    display: flex; align-items: center; justify-content: center;
  }
  .card--front { top: 470px; background: var(--paper); }

  .brand { display: flex; align-items: center; gap: 14px; }
  .brand__mark { width: 46px; height: 46px; background: #e6e6e6; }
  .brand__name {
    font-weight: 700; font-size: 62px; letter-spacing: 2px; line-height: 1;
    color: #e6e6e6;
  }
  .card--front .brand { position: absolute; left: 250px; top: 48px; }
  .card--front .brand__name { color: var(--silver-dark); font-size: 56px; }
  .card--front .brand__mark { width: 40px; height: 40px; background: var(--silver-dark); }

  .address {
    position: absolute; right: 36px; top: 150px; text-align: right;
    font-style: normal; font-size: 15px; line-height: 21px; color: var(--ink);
  }
  .rule {
    position: absolute; left: 36px; right: 36px; top: 202px;
    height: 1px; background: var(--rule);
  }
  .person { position: absolute; left: 36px; top: 214px; color: var(--ink); }
  .person__name {
    font-weight: 700; font-size: 16px; line-height: 22px;
    letter-spacing: .5px; margin-bottom: 6px;
  }
  .contact { display: flex; align-items: center; gap: 9px; font-size: 15px; line-height: 22px; }
  .contact svg { width: 13px; height: 13px; fill: var(--ink); flex: none; }
  .web-band {
    position: absolute; left: 0; right: 0; bottom: 16px; height: 34px;
    background: linear-gradient(90deg, #ffffff 0%, #e4e4e4 30%, var(--silver-light) 70%, var(--silver) 100%);
    display: flex; align-items: center; justify-content: flex-end; padding-right: 40px;
  }
  .web-band__url {
    font-size: 16px; font-weight: 600; letter-spacing: 7px; color: #f4f4f4;
  }
  .base-line {
    position: absolute; left: 0; right: 0; bottom: 6px; height: 4px;
    background: var(--silver-light);
  }
</style>
</head>
<body>
<main class="canvas">
  <section class="card card--back" aria-label="Rückseite">
    <div class="brand">
      <span class="brand__mark"></span>
      <span class="brand__name">TKWL</span>
    </div>
  </section>

  <section class="card card--front" aria-label="Vorderseite">
    <div class="brand">
      <span class="brand__mark"></span>
      <span class="brand__name">TKWL</span>
    </div>
    <address class="address">Kellbacher Str. 38<br>74819 Haldenberg</address>
    <div class="rule"></div>
    <div class="person">
      <p class="person__name">JONAS WEBER</p>
      <p class="contact">
        <svg viewBox="0 0 24 24" aria-hidden="true"><path d="M6.6 10.8a15.1 15.1 0 0 0 6.6 6.6l2.2-2.2a1 1 0 0 1 1-.25 11.4 11.4 0 0 0 3.6.57 1 1 0 0 1 1 1V20a1 1 0 0 1-1 1A17 17 0 0 1 3 4a1 1 0 0 1 1-1h3.5a1 1 0 0 1 1 1c0 1.25.2 2.45.57 3.57a1 1 0 0 1-.25 1z"/></svg>
        07162-418395-0
      </p>
      <p class="contact">
        <svg viewBox="0 0 24 24" aria-hidden="true"><path d="M2 5h20v14H2z M2 5l10 8 10-8" fill="none" stroke="#7a7a7a" stroke-width="2"/><path d="M3 6l9 7 9-7v12H3z"/></svg>
        Name@service-tkwl.de
      </p>
    </div>
    <div class="web-band"><span class="web-band__url">www.service-tkwl.de</span></div>
    <div class="base-line"></div>
  </section>
</main>
</body>
</html>
```